Label design for ecological olive oil from an innovative farm in Spain

EL PRADO SOLAR - Olive Oil Label
El Prado Solar is a small farm in southern Spain dedicated to regenerative, ecological and syntropic agriculture. We are launching a new extra virgin olive oil and, alongside it, a renewed brand identity that reflects our relationship with land, life and earth.
Our farm works as a living food forest: diverse, dense, colourful and abundant. This is not industrial organic farming — it is ecosystem regeneration in action. We are looking for a label that feels:
* Lush, abundant and alive
* Nature-connected and animist (the land as a living being)
* Sunny Mediterranean (southern Spain, warmth, light, joy)
* Upbeat and playful, not austere or “eco-serious”
* Slightly rebellious, non-corporate, non-industrial
This is an olive oil for people who care deeply about the planet, but who also love beauty, colour and pleasure.
We are particularly drawn to designs that express the visual richness and lushness of our syntropic food forest:
* Dense, layered plant life
* Multiple tree species growing together
* A sense of abundance
* A “window into a living world” feeling
Tree species present on the farm include:
* Olive
* Citrus
* Pomegranate
* Fig
* Almond
We welcome designs with illustrative approaches that feel hand-drawn, painterly or slightly retro. We are open to interpretation — the goal is to transmit aliveness, not literal realism.
We currently use Montserrat font and are happy to continue with it or something similar.
We are also open to retro-inspired or softer typefaces, provided they feel natural, warm and not corporate.
We want to avoid plastic labels. The design should work with:
* Uncoated/organic paper labels, or
* Direct printing or screen printing onto glass
The label should feel tactile and natural.
We have uploaded :
* Final front and back label text (Spanish + English)
* Logo
* Reference images (AI explorations, farm photos, landscape, food forest)
The olive oil will be sold in Spain and internationally, so bilingual clarity is important.
Our business logo should be used but does not need to dominate the front label.
It may work better subtly placed, possibly on the back label or integrated quietly into the design.
A successful label will feel like:
* A living landscape captured on a bottle
* Something joyful, rooted and contemporary
* A product of land, care and imagination — not marketing
We want people to feel, instinctively:
This oil comes from a place that is alive.

```html
<!DOCTYPE html>
<html lang="es">
<head>
<meta charset="utf-8">
<title>El Prado Solar – Olive Oil Label</title>
<link href="https://fonts.googleapis.com/css2?family=Crimson+Pro:wght@400;600&display=swap" rel="stylesheet">
<style>
  :root {
    --page-bg: #ececec;
    --label-bg: #1f2817;
    --foliage-mid: rgba(84, 102, 50, 0.55);
    --foliage-soft: rgba(70, 86, 44, 0.45);
    --foliage-warm: rgba(128, 124, 58, 0.28);
    --gold: #c6a574;
    --accent-line: #8a8f3a;
    --sun: #e8963a;
    --sun-glow: rgba(232, 150, 58, 0.35);
    --cream: #f3efe4;
  }
  * { margin: 0; padding: 0; box-sizing: border-box; }
  html, body {
    width: 1200px;
    height: 1200px;
    overflow: hidden;
    background: var(--page-bg);
  }
  .label {
    position: absolute;
    left: 264px;
    top: 95px;
    width: 673px;
    height: 1010px;
    background: var(--label-bg);
    overflow: hidden;
    font-family: "Crimson Pro", "Times New Roman", serif;
    color: var(--cream);
    text-align: center;
  }
  .foliage-left {
    position: absolute;
    left: 0;
    top: 0;
    width: 190px;
    height: 1010px;
    background:
      radial-gradient(ellipse 60% 14% at 40% 12%, var(--foliage-mid), transparent 75%),
      radial-gradient(ellipse 55% 12% at 30% 30%, var(--foliage-soft), transparent 75%),
      radial-gradient(ellipse 60% 13% at 45% 48%, var(--foliage-mid), transparent 75%),
      radial-gradient(ellipse 50% 10% at 55% 62%, var(--foliage-warm), transparent 75%),
      radial-gradient(ellipse 60% 13% at 35% 76%, var(--foliage-soft), transparent 75%),
      radial-gradient(ellipse 55% 11% at 45% 92%, var(--foliage-mid), transparent 75%);
  }
  .foliage-top {
    position: absolute;
    left: 0;
    top: 0;
    width: 673px;
    height: 230px;
    background:
      radial-gradient(ellipse 18% 45% at 30% 30%, var(--foliage-soft), transparent 75%),
      radial-gradient(ellipse 16% 50% at 52% 20%, var(--foliage-mid), transparent 75%),
      radial-gradient(ellipse 18% 45% at 72% 25%, var(--foliage-warm), transparent 75%),
      radial-gradient(ellipse 16% 40% at 90% 10%, var(--foliage-soft), transparent 75%);
  }
  .brand {
    position: absolute;
    left: 0;
    right: 0;
    top: 196px;
  }
  .brand-sun {
    display: block;
    margin: 0 auto 34px;
    filter: drop-shadow(0 0 14px var(--sun-glow));
  }
  .brand-name {
    font-weight: 600;
    font-size: 44px;
    line-height: 50px;
    letter-spacing: 2px;
    color: var(--gold);
  }
  .product-name,
  .claim {
    position: absolute;
    left: 0;
    right: 0;
    font-size: 28px;
    line-height: 36px;
  }
  .product-name { top: 488px; }
  .claim-es { top: 656px; }
  .claim-en { top: 754px; }
  .volume {
    position: absolute;
    left: 0;
    right: 0;
    top: 922px;
    font-size: 25px;
    line-height: 36px;
    letter-spacing: 2px;
  }
  .frame-line {
    position: absolute;
    left: 0;
    top: 0;
  }
</style>
</head>
<body>
  <main class="label">
    <div class="foliage-left" role="img" aria-label="Hand-drawn olive branches with leaves, olives and blossoms climbing the left edge"></div>
    <div class="foliage-top" role="img" aria-label="Hand-drawn olive leaves and fruit spreading along the top edge"></div>

    <svg class="frame-line" width="673" height="1010" viewBox="0 0 673 1010" aria-hidden="true">
      <polyline points="611,255 611,946 483,946" fill="none" stroke="var(--accent-line)" stroke-width="2"/>
    </svg>

    <div class="brand">
      <svg class="brand-sun" width="58" height="58" viewBox="0 0 58 58" aria-hidden="true">
        <circle cx="29" cy="29" r="28" fill="var(--sun)"/>
      </svg>
      <div class="brand-name">EL PRADO SOLAR</div>
    </div>

    <p class="product-name">Aceite de Oliva Virgen Extra<br>Extra Virgin Olive Oil</p>
    <p class="claim claim-es">Cultivado con practicas de la<br>agricultura regenerativa y sintrópica</p>
    <p class="claim claim-en">Grown using regenerative and<br>syntropic farming practices</p>
    <p class="volume">750 ml</p>
  </main>
</body>
</html>
```